Rise As Captain Book Cover Design

Book Cover Design Brief
Book Title
Rise As Captain
Subtitle
The 10 Quiet Habits of Remarkable Command
Author
Orwen Dalquist
Overview
This book is about leadership that starts within.
Most leadership books focus on tactics or management strategies. This book focuses on the inner disciplines that create powerful leaders — mindset, integrity, focus, empathy, professionalism, honesty, and self-respect.
The tone of the book is bold, direct, confident, and transformational.
This is not a soft or corporate leadership book. It is a call to step up and become the leader you are capable of becoming.
The cover should feel:
• Powerful
• Professional
• Transformational
• Premium
• Memorable
Think best-selling leadership book, not a generic business book.
Target Audience
Business owners
Managers
Entrepreneurs
Team leaders
Professionals who want to grow as leaders
Most readers are ambitious professionals who want to level up their leadership and life.
Design Direction
The design should communicate:
Strength. Discipline. Leadership. Personal transformation.
Avoid cliché leadership visuals like:
• Handshakes
• Office buildings
• Corporate stock imagery
• Teams sitting around tables
The design should feel iconic, bold, and timeless.
Think about covers of successful leadership books such as:
Copper Rituals
Total Stewardship
Won't Break Now
Begin From Purpose
The 36 Rules of Sway
These covers are simple, powerful, and recognizable even at small sizes.
Typography
The title RISE AS CAPTAIN should be:
• Bold
• Strong
• Dominant on the cover
• Easy to read even at small sizes (important for Vellora thumbnails)
The subtitle should be clean and secondary to the title.
The overall typography should feel strong, modern, and premium.
Color Direction
Designers are free to explore colors, but the cover should feel strong and premium, not playful.
Colors that often work well for leadership books include:
Black
Gold
White
Deep blue
Dark red
High contrast and clarity are important.
Style
Preferred style:
• Clean
• Modern
• Minimal
• Strong contrast
Avoid clutter and overly busy designs.
The goal is to create a cover that feels powerful and professional at first glance.
Deliverables
Front cover design for a leadership book.
Final files should include:
• High resolution artwork
• Editable source files
• Print-ready version suitable for publishing
Goal of the Cover
When someone sees this book on Vellora or in a bookstore, they should immediately think:
“This looks like a serious leadership book.”
The design should feel like it belongs next to books by authors such as:
Marcus Thorley
Brandt Osgood
Peter Hollis
Nolan Fairbrook
A strong, confident cover that attracts leaders who want to grow and perform at a higher level.
Target Market(s)
Business Owners and High level managers
Look and feel
Each slider illustrates characteristics of the customer's brand and the style your logo design should communicate.

```html
<!DOCTYPE html>
<html lang="en">
<head>
<meta charset="utf-8">
<title>Rise As Captain — Book Cover</title>
<link href="https://fonts.googleapis.com/css2?family=Anton&family=Montserrat:wght@900&family=Oswald:wght@500;700&display=swap" rel="stylesheet">
<style>
  :root {
    --navy: #0b0536;
    --red: #a50d0d;
    --red-deep: #8a0606;
    --paper: #ececec;
    --paper-light: #fafafa;
    --stage: #d9d9d9;
    --white: #ffffff;
  }
  * { margin: 0; padding: 0; box-sizing: border-box; }
  html, body {
    width: 1200px;
    height: 800px;
    overflow: hidden;
    background: var(--stage);
  }
  .canvas {
    position: relative;
    width: 1200px;
    height: 800px;
  }
  .book-cover {
    position: absolute;
    left: 345px;
    top: 20px;
    width: 510px;
    height: 760px;
    background: linear-gradient(120deg, var(--paper) 0%, var(--paper-light) 45%, var(--paper) 100%);
    box-shadow: 0 6px 22px rgba(0,0,0,0.18);
    overflow: hidden;
  }
  .collar-tie-art {
    position: absolute;
    left: 238px;
    top: 26px;
    width: 242px;
    height: 480px;
    background: linear-gradient(180deg, var(--navy) 0%, var(--navy) 35%, var(--red) 65%, var(--red-deep) 100%);
  }
  .title-art {
    position: absolute;
    left: 0;
    top: 0;
    width: 510px;
    height: 760px;
  }
  .title-word {
    font-family: 'Anton', 'Oswald', sans-serif;
    fill: var(--navy);
  }
  .title-lead {
    font-family: 'Montserrat', sans-serif;
    font-weight: 900;
    fill: var(--white);
  }
  .subtitle {
    position: absolute;
    left: 236px;
    top: 545px;
    width: 260px;
    font-family: 'Oswald', sans-serif;
    font-weight: 500;
    font-size: 21px;
    line-height: 1.08;
    color: var(--red);
    text-transform: uppercase;
  }
  .author {
    position: absolute;
    left: 236px;
    top: 614px;
    font-family: 'Oswald', sans-serif;
    font-weight: 700;
    font-size: 37px;
    line-height: 1;
    color: var(--navy);
    text-transform: uppercase;
    letter-spacing: -0.5px;
    white-space: nowrap;
  }
</style>
</head>
<body>
  <main class="canvas">
    <article class="book-cover">
      <div class="collar-tie-art" role="img" aria-label="Illustration area: navy shirt collar with a red necktie hanging down"></div>

      <svg class="title-art" viewBox="0 0 510 760" aria-label="Rise As Captain">
        <text class="title-word" transform="translate(220,738) rotate(-90)"
              font-size="228" textLength="712" lengthAdjust="spacingAndGlyphs">CAPTAIN</text>
        <rect x="30" y="150" width="192" height="66" fill="var(--navy)" stroke="var(--paper-light)" stroke-width="5"/>
        <text class="title-lead" x="126" y="197" font-size="40" text-anchor="middle"
              textLength="164" lengthAdjust="spacingAndGlyphs">RISE AS</text>
      </svg>

      <p class="subtitle">The 10 Quiet Habits of<br>Remarkable Command</p>
      <p class="author">Orwen Dalquist</p>
    </article>
  </main>
</body>
</html>
```